Strong Pulse, Clear Mind Poster for American Indian Older Adults

We need am 11" x 17" poster designed for a health outreach project designed to reach older U.S. American Indians. The materials developed through this project will be distributed to American Indian and Alaska Native tribes, communities and tribal-serving organizations across the U.S. (more than 500 different tribes). If we find a successful design we will work with that designer to produce at least one other item we need design work for using the same look/feel and maybe other materials for this project. (more work!). The poster will include a set of facts (bulleted list on the attached document) that we would like presented in an "infographic" style. The design must be reflective of the American Indian culture and designed with older adults (65 and older) in mind. Imagery plays a strong role in the American Indian culture in the U.S. images of the heart, water, feathers, circle of life, etc. If you use photos of people they must include older adults and they must be American Indian (Native American). We prefer deep earth tones for the color scheme. The design must take into account design principles for older adults: 1. Try not to put colored font on colored background 2. Ensure high contrast for text 3. Font style should be sans serif, not cursive,decorative or heavily stylized because it is harder to read 4. Avoid using all caps 5. Don't print sideways or on top of images, shaded, backgrounds, etc. 6. All images should related specifically to the content of the text and be culturally appropriate for both older adults and American Indians. The final design should be easy to read and appeal to older American Indian adults. We need to incorporate three logos on the poster towards the bottom they should not be the center/focus of the poster. We also need to include a statement about who produced the materials- that can be very small below the logos at the bottom of the poster. We've attached the text for the poster and three logo files (note one is solid blue- we will finalize that after the document design is selected but need a placeholder for that logo.

Target Market(s)

Older adult (65 and older) American Indian and Alaska Natives and their family members in tribes, communities and tribal-serving organizations across the US

Font styles to use
Sans Serif

Requirements
Must have
• Must adhere to good design principles for older adults (listed in project description)
• Must feature culturally appropriate/targeted imagery and design look and feel

```html
<!DOCTYPE html>
<html lang="en">
<head>
<meta charset="utf-8">
<title>Strong Pulse, Clear Mind</title>
<link href="https://fonts.googleapis.com/css2?family=Oswald:wght@500;600&family=Montserrat:wght@500;600;700&display=swap" rel="stylesheet">
<style>
  :root {
    --red: #c8070d;
    --white: #ffffff;
    --ink: #3a3a3a;
    --mist: #d9d5bb;
    --moss: #5d6a4f;
    --forest: #243227;
    --deep: #1c241e;
    --logo-orange: #d2521d;
    --logo-blue: #2b6cb0;
    --logo-green: #1f9a4a;
  }
  * { box-sizing: border-box; margin: 0; padding: 0; }
  html, body { width: 880px; height: 1200px; overflow: hidden; background: var(--deep); }
  .poster {
    position: relative; width: 880px; height: 1200px; overflow: hidden;
    font-family: "Montserrat", sans-serif; color: var(--white);
  }
  .forest-backdrop {
    position: absolute; inset: 0;
    background:
      radial-gradient(ellipse 300px 320px at 50% 30%, rgba(230,226,200,.55), transparent 70%),
      linear-gradient(180deg, var(--mist) 0%, #b9b797 22%, var(--moss) 45%, var(--forest) 70%, var(--deep) 100%);
  }
  .title { position: absolute; font-family: "Oswald", sans-serif; font-weight: 600; line-height: 1; text-transform: uppercase; }
  .title-left { left: 60px; top: 96px; width: 385px; text-align: center; }
  .title-left .line1 { color: var(--ink); font-size: 104px; letter-spacing: -1px; }
  .title-left .line2 { color: var(--white); font-size: 136px; margin-top: -2px; letter-spacing: -1px; }
  .title-box {
    left: 455px; top: 104px; width: 372px; height: 209px; background: var(--white);
    text-align: center; padding-top: 0;
  }
  .title-box .line1 { color: var(--ink); font-size: 104px; margin-top: -8px; }
  .title-box .line2 { color: var(--red); font-size: 136px; margin-top: -4px; }
  .tagline {
    position: absolute; left: 0; right: 0; top: 342px; text-align: center;
    font-size: 37px; font-weight: 600; line-height: 48px;
    text-shadow: 0 2px 6px rgba(0,0,0,.45);
  }
  .divider { position: absolute; left: 404px; top: 512px; width: 72px; height: 3px; background: var(--white); }
  .marker { position: absolute; width: 130px; height: 150px; }
  .fact {
    position: absolute; width: 190px; text-align: center;
    font-size: 19px; font-weight: 700; line-height: 26px;
    text-shadow: 0 1px 4px rgba(0,0,0,.5);
  }
  .alert-band {
    position: absolute; left: 10px; top: 936px; width: 851px; height: 99px;
    background: var(--red); text-align: center;
    font-size: 23px; font-weight: 500; line-height: 28px; padding-top: 8px;
  }
  .call-to-action {
    position: absolute; left: 0; right: 0; top: 1050px; text-align: center;
    font-size: 21px; font-weight: 700; line-height: 30px; color: var(--red);
  }
  .call-to-action strong { color: var(--white); }
  .partner-bar {
    position: absolute; left: 0; right: 0; top: 1126px; height: 74px; background: var(--white);
    display: flex; align-items: center; justify-content: center; gap: 42px;
  }
  .partner { display: flex; align-items: center; gap: 8px; font-family: "Montserrat", sans-serif; font-weight: 700; font-size: 20px; }
  .partner-one { color: var(--logo-orange); }
  .partner-three { color: var(--logo-green); font-size: 15px; }
  .partner-dot { width: 14px; height: 14px; border-radius: 50%; background: var(--logo-orange); }
  .partner-square { width: 14px; height: 14px; background: var(--logo-green); }
  .partner-placeholder { width: 70px; height: 52px; border: 2px solid var(--logo-blue); }
</style>
</head>
<body>
<main class="poster">
  <div class="forest-backdrop" role="img" aria-label="Misty evergreen forest photograph with a soft heart shape formed in the fog"></div>

  <h1 class="title title-left"><span class="line1" style="display:block">Strong</span><span class="line2" style="display:block">Pulse</span></h1>
  <div class="title title-box"><span class="line1" style="display:block">Clear</span><span class="line2" style="display:block">Mind</span></div>

  <p class="tagline">The River of Life Flows<br>Through the Heart, Protecting<br>the Mind and Body</p>
  <div class="divider"></div>

  <!-- fact markers -->
  <svg class="marker" style="left:74px;top:600px" viewBox="0 0 130 150" aria-hidden="true">
    <path d="M65 137 L52 118 L78 118 Z" fill="var(--red)"/>
    <circle cx="65" cy="65" r="57" fill="none" stroke="var(--red)" stroke-width="8"/>
    <text x="65" y="94" text-anchor="middle" font-family="Montserrat, sans-serif" font-weight="700" font-size="82" fill="var(--white)">1</text>
  </svg>
  <svg class="marker" style="left:264px;top:732px" viewBox="0 0 130 150" aria-hidden="true">
    <path d="M65 6 L52 26 L78 26 Z" fill="var(--white)"/>
    <circle cx="65" cy="80" r="57" fill="none" stroke="var(--white)" stroke-width="8"/>
    <text x="65" y="109" text-anchor="middle" font-family="Montserrat, sans-serif" font-weight="700" font-size="82" fill="var(--red)">2</text>
  </svg>
  <svg class="marker" style="left:459px;top:600px" viewBox="0 0 130 150" aria-hidden="true">
    <path d="M65 137 L52 118 L78 118 Z" fill="var(--red)"/>
    <circle cx="65" cy="65" r="57" fill="none" stroke="var(--red)" stroke-width="8"/>
    <text x="65" y="94" text-anchor="middle" font-family="Montserrat, sans-serif" font-weight="700" font-size="82" fill="var(--white)">3</text>
  </svg>
  <svg class="marker" style="left:671px;top:741px" viewBox="0 0 130 150" aria-hidden="true">
    <path d="M65 6 L52 26 L78 26 Z" fill="var(--white)"/>
    <circle cx="65" cy="80" r="57" fill="none" stroke="var(--white)" stroke-width="8"/>
    <text x="65" y="109" text-anchor="middle" font-family="Montserrat, sans-serif" font-weight="700" font-size="82" fill="var(--red)">4</text>
  </svg>

  <p class="fact" style="left:234px;top:641px">Alzheimer’s is the 6th leading cause of death</p>
  <p class="fact" style="left:46px;top:760px">5.7 million Americans have Alzheimer’s disease</p>
  <p class="fact" style="left:429px;top:760px">1 out 10 people age 65 and older has Alzheimer’s</p>
  <p class="fact" style="left:632px;top:618px;width:202px;line-height:23px">1 out of 3 American Indians over 65 develop dementia, including Alzheimer’s</p>

  <p class="alert-band">Elders with diabetes, heart disease, or high blood<br>pressure have a much higher risk of developing Alzheimer’s<br>or other dementias</p>

  <p class="call-to-action"><strong>Make an appointment</strong> with your doctor today to talk<br>about how to keep your mind and heart healthy.</p>

  <footer class="partner-bar">
    <div class="partner partner-one"><span class="partner-dot"></span>Northwind Health</div>
    <div class="partner-placeholder" aria-label="Partner logo placeholder"></div>
    <div class="partner partner-three"><span class="partner-square"></span>Cedar Circle Elders</div>
  </footer>
</main>
</body>
</html>
```